Morvex Business Card (intended for Business Card sized magnet)

Hi guys,

I would like to get a design for my business card for the restaurant. The design must be single sided as I intend to produce business card sized magnets.

The File attached must me on and I'm open for new ides

Can you please ensure that the design meets Cardowell's magnetic business card size specifications:

http://www.cardowell.example.au/custom-magnets.aspx?txi=15695&xnid=TopNav_Magnetic+Business+Cards+(linked+item)_Magnets_Marketing+Products&xnav=TopNav

Full Bleed Size (starting document size):
90 x 52 mm
1062 x 615 pixels
* Finished artwork should use the full bleed dimensions for best results.

Document Trim Size (final size after being cut):
87 x 49 mm
1028 x 579 pixels
* Please be sure to keep all text within the safe margin.

Resolution:
300 DPI

The winning design/source files need to meet these specifications.

Thanks
Updates

Hi guys, can I see more options please Thanks

```html
<!DOCTYPE html>
<html lang="en">
<head>
<meta charset="utf-8">
<title>Morvex Business Card</title>
<link rel="stylesheet" href="https://fonts.googleapis.com/css2?family=Crimson+Text:wght@400&family=Noto+Serif:wght@400&family=Oswald:wght@600&display=swap">
<style>
  :root {
    --ink: #0b0b0b;
    --paper: #ffffff;
    --red: #c1272d;
    --teal: #1ea5b5;
    --body: #464646;
  }
  html, body {
    margin: 0;
    padding: 0;
    width: 1200px;
    height: 730px;
    overflow: hidden;
    background: var(--paper);
  }
  .card {
    position: relative;
    width: 1200px;
    height: 730px;
    background: var(--paper);
    overflow: hidden;
  }
  .brand-panel {
    position: absolute;
    left: 0;
    top: 0;
    width: 494px;
    height: 730px;
    background: var(--ink);
  }
  .brand-name {
    position: absolute;
    left: 0;
    width: 494px;
    top: 212px;
    margin: 0;
    text-align: center;
    font-family: "Crimson Text", serif;
    font-weight: 400;
    font-size: 112px;
    line-height: 1;
    color: var(--paper);
  }
  .rule {
    position: absolute;
    left: 74px;
    width: 390px;
    height: 5px;
    background: var(--paper);
  }
  .rule--top { top: 362px; }
  .rule--bottom { top: 488px; }
  .pattern-band {
    position: absolute;
    left: 74px;
    top: 376px;
    width: 390px;
    height: 102px;
    background: linear-gradient(90deg, #2a2a2a, #3a3a3a 50%, #2a2a2a);
  }
  .call-now {
    position: absolute;
    right: 19px;
    top: 66px;
    margin: 0;
    font-family: "Crimson Text", serif;
    font-size: 43px;
    line-height: 1;
    color: var(--red);
    white-space: nowrap;
  }
  .call-now .phone {
    font-family: "Oswald", sans-serif;
    font-weight: 600;
    font-size: 40px;
  }
  .dish-area {
    position: absolute;
    left: 671px;
    top: 184px;
    width: 375px;
    height: 143px;
    background: linear-gradient(180deg, #e6e6e6, #cfcfcf);
  }
  .licence {
    position: absolute;
    left: 671px;
    width: 375px;
    top: 336px;
    margin: 0;
    text-align: center;
    font-family: "Crimson Text", serif;
    font-size: 27px;
    color: var(--ink);
  }
  .venue-name {
    position: absolute;
    left: 531px;
    top: 424px;
    margin: 0;
    font-family: "Noto Serif", serif;
    font-weight: 400;
    font-size: 52px;
    line-height: 1.1;
    color: var(--teal);
  }
  .details {
    position: absolute;
    left: 535px;
    top: 492px;
    margin: 0;
    padding: 0;
    list-style: none;
    font-family: "Noto Serif", serif;
    font-size: 25px;
    line-height: 35px;
    color: var(--body);
    white-space: nowrap;
  }
  .details .indent { padding-left: 221px; }
</style>
</head>
<body>
  <div class="card">
    <div class="brand-panel">
      <h1 class="brand-name">Morvex</h1>
      <div class="rule rule--top"></div>
      <div class="pattern-band" role="img" aria-label="Decorative geometric star pattern band with red, teal and yellow accents"></div>
      <div class="rule rule--bottom"></div>
    </div>

    <p class="call-now">Call Now - <span class="phone">03 9481 2230</span></p>

    <div class="dish-area" role="img" aria-label="Illustration of a covered serving dish"></div>
    <p class="licence">Fully Licenced &amp; BYO</p>

    <h2 class="venue-name">Morvex Restrurant</h2>
    <ul class="details">
      <li>214 Larkspur Rd, Elsdale South ,3190</li>
      <li>Log on to : www.morvex.example.au</li>
      <li>Email Us : Morvex214@mailbox.example</li>
      <li>Opening Hours : Sunday - Friday 11:30 -9:30</li>
      <li class="indent">Saturday from 5:30 -10.00</li>
    </ul>
  </div>
</body>
</html>
```